Brochure Design Project

hi
Im looking for a great little design for my brochures. I have a home beauty salon and need a brochure menu. The name of the business is Kanoha SoftGlow which is a japanese name. I'm not japanese but want it to have a slight feel of japanese, perhaps some watercolour or a traditional pattern.
Salon menu will have waxing, Facials, massage etc and would like a tri fold brochure
No bright colours please or butterflies. I want it to look and feel relaxing and peaceful. Help with a nice Logo would also be great
thanks for your help
Updates

Project Deadline Extended
Reason: I know a lot of you are busy but by extending the timeframe I can hopefully get all your creative minds flowing

hi

Just thought I'd add that I would like the brochures to be modern and edgy looking
thanks so far

Target Market(s)

People that want to be pampered and look and feel great and have a sort of natural feel ( if that makes sense)

Industry/Entity Type

Beauty Salon

Requirements
Must have
• I would like it to be A4 size and folded as a tri brochure,
Nice to have
• A classy font
Should not have
• Butterflies, swirls, bright colours or purple

```html
<!DOCTYPE html>
<html lang="en">
<head>
<meta charset="utf-8">
<title>Kanoha SoftGlow – Service Menu</title>
<link href="https://fonts.googleapis.com/css2?family=Raleway:wght@200;300&family=Lato:wght@400;700&display=swap" rel="stylesheet">
<style>
  :root{
    --mint:#c3e2d2;
    --mint-deep:#9fc9b5;
    --mint-label:#a3cdb9;
    --photo-a:#7fa596;
    --photo-b:#cfe6da;
    --ink:#3b322c;
    --paper:#ffffff;
    --page:#ffffff;
  }
  *{margin:0;padding:0;box-sizing:border-box}
  html,body{width:848px;height:1200px;overflow:hidden;background:var(--page)}
  body{position:relative;font-family:'Lato',sans-serif;color:var(--ink)}
  .spread{position:absolute;left:34px;width:780px;background:var(--paper);box-shadow:0 3px 10px rgba(0,0,0,.25)}
  .spread--outside{top:20px;height:556px}
  .spread--inside{top:605px;height:557px}
  .panel{position:absolute;top:0;width:260px;height:100%;overflow:hidden}
  .panel--1{left:0}.panel--2{left:260px}.panel--3{left:520px}
  .photo{position:absolute;left:0;width:260px;background:linear-gradient(135deg,var(--photo-b),var(--photo-a))}
  .photo--head{top:0;height:139px}
  .spread--inside .photo--head{height:127px}
  .photo-title{position:absolute;left:28px;bottom:4px;font-family:'Raleway',sans-serif;font-weight:200;font-size:22px;color:#fff;letter-spacing:.5px}
  .menu{position:absolute;left:30px;right:28px;font-size:7.6px;line-height:1.3}
  .item{color:var(--mint-label);margin-bottom:9px}
  .item b{color:var(--ink);font-weight:700}
  .desc{margin:-2px 0 9px;text-align:justify}
  .note{margin-bottom:9px}
  .brand{font-family:'Raleway',sans-serif;font-weight:300;color:var(--ink);white-space:nowrap;display:flex;align-items:center;gap:7px}
  .brand .dot{width:9px;height:9px;border-radius:50%;background:var(--mint-deep)}
  .contact{position:absolute;left:0;width:260px;top:352px;text-align:center;font-size:10.5px;line-height:1.45}
  .contact .brand{justify-content:center;font-size:23px;margin-bottom:22px}
  .contact h3{font-size:11px;font-weight:700;margin-bottom:14px;letter-spacing:.5px}
  .cover{position:absolute;left:0;top:139px;width:260px;height:251px;background:var(--mint)}
  .cover .brand{position:absolute;left:40px;top:70px;font-size:24px;color:#fff}
  .cover .brand .dot{background:#fff}
  .cover-title{position:absolute;left:0;width:260px;text-align:center;top:118px;font-family:'Raleway',sans-serif;font-weight:200;color:#fff;line-height:.95}
  .cover-title .l1{display:block;font-size:40px}
  .cover-title .l2{display:block;font-size:60px}
  .photo--foot{top:390px;height:166px}
  .section-title{font-family:'Raleway',sans-serif;font-weight:300;font-size:28px;color:var(--ink);margin:4px 0 8px}
  .price-list{list-style:none;font-size:8px;font-weight:700}
  .price-list li{margin-bottom:17.3px}
  .fade{position:absolute;left:30px;bottom:0;width:200px;height:115px;background:radial-gradient(ellipse at 60% 70%,rgba(159,201,181,.55),rgba(255,255,255,0) 70%)}
</style>
</head>
<body>

<section class="spread spread--outside">
  <div class="panel panel--1">
    <div class="photo photo--head" role="img" aria-label="Close-up photo of closed eyes with tinted lashes"><span class="photo-title">EYES</span></div>
    <div class="menu" style="top:158px">
      <p class="item">Lash tint <b>$15.00</b></p>
      <p class="item">Brow tint <b>$12.00</b></p>
    </div>
  </div>

  <div class="panel panel--2">
    <div class="photo photo--head" role="img" aria-label="Photo of a foot massage"><span class="photo-title">FOR YOUR FEET</span></div>
    <div class="menu" style="top:158px">
      <p class="item">Play with my feet massage <b>15 min $15.00</b></p>
      <p class="item">Ahh Bliss</p>
      <p class="item">Kanzen Feet means perfection complete <b>$50.00</b></p>
      <p class="desc">The ultimate foot therapy concentrates on the feet to reduce stress and tension. Consists of a cleansing soak, invigorating sea salt foot scrub, massage and foot mask, ending with a hot towel. A great stress reliever after a long day.</p>
    </div>
    <div class="contact">
      <div class="brand"><span class="dot"></span>Kanoha SoftGlow</div>
      <h3>CONTACT</h3>
      <p>MARA ELLISON<br>PH:0400 123 456</p>
    </div>
  </div>

  <div class="panel panel--3">
    <div class="photo photo--head" role="img" aria-label="Photo of hot stones on a back by water"></div>
    <div class="cover">
      <div class="brand"><span class="dot"></span>Kanoha SoftGlow</div>
      <h1 class="cover-title"><span class="l1">SERVICE</span><span class="l2">MENU</span></h1>
    </div>
    <div class="photo photo--foot" role="img" aria-label="Photo of bowls of body butter"></div>
  </div>
</section>

<section class="spread spread--inside">
  <div class="panel panel--1">
    <div class="photo photo--head" role="img" aria-label="Photo of a facial mask being applied with a brush"><span class="photo-title">FACIALS</span></div>
    <div class="menu" style="top:142px">
      <p class="item">Hayai Facial <b>$40.00</b></p>
      <p class="item">Series of 3 <b>$105.00</b></p>
      <p class="desc">When time is of the essence, this Express Facial treatment will revitalise your skin's radiance, leaving it with a ealthy glow. Includes cleansing, exfoliation, pressure point massage, moisturiser and sunscreen.</p>
      <p class="note">Allow 30 min</p>
      <p class="item">Vitamin C facial Brightening treatment <b>$70.00</b></p>
      <p class="item">Series of 3 <b>$190.00</b></p>
      <p class="desc">This facial treatment uses a concentrated complex of topical vitamin C that is easily absorbed by the skin. This helps battle the visible signs of ageing. This formulation has been proven in the medical field to be an antioxidant that works by mopping up damaging chemical compounds known as "free radicals." This topical antioxidant also stimulates the production of collagen.</p>
      <p class="note">Allow 1hr</p>
      <p class="item">Kanoha Signature Facial <b>$75.00</b></p>
      <p class="item">Series of 3 <b>$200.00</b></p>
      <p class="desc">Enjoy an hour of total relaxation and emerge looking and feeling great! This facial is the ultimate for the over worked and over stressed. Your customised facial will begin with a deep cleanse, followed by a gentle exfoliation, mask, massage and completed with a nourishing moisturizer and eye crème.</p>
      <p class="note">Allow 1 hr</p>
    </div>
  </div>

  <div class="panel panel--2">
    <div class="fade" role="img" aria-label="Faded photo of a woman relaxing during a massage"></div>
    <div class="menu" style="top:18px">
      <p class="item">Kanoha Ultimate Tranquility <b>$95.00</b></p>
      <p class="desc">This blissful treatment starts with a dry body brush, jojoba oil is then drizzled over the back, followed by a completely relaxing hot stone back massage. To finish off, your skin is treated to a indulgently nourishing facial.</p>
      <p class="note">Allow 1 hr 15min</p>
      <p class="item">Kanoha Man <b>$70.00</b></p>
      <p class="item">Series of 3 <b>$190.00</b></p>
      <p class="desc">Maintain the vitality and look of healthy skin with a double cleanse, exfoliate facial massage, and a hydrating mask.</p>
      <p class="item">Bare Back Purification <b>$50.00</b></p>
      <p class="desc">This includes a deep cleanse. Exfoliation, extractions, mask and moisturizer to leave your back feeling smooth and refreshed.</p>
      <p class="note">Allow 30min</p>
      <h2 class="section-title">MASSAGE</h2>
      <p class="item">Full body Hot Stone Massage <b>$85.00</b></p>
      <p class="desc">This treatment melts away tension with smooth warm basalt stones and will put you in the ultimate relaxed state</p>
      <p class="note">Allow 1hr</p>
      <p class="item">Body massage <b>$60.00</b></p>
      <p class="desc">Relaxing the body as well as the mind will rejuvenate and awaken your spirit. Choose a Relaxation, Swedish or Aromatherapy massage.</p>
      <p class="note">Allow 1 hr</p>
      <p class="item">Back Massage <b>$50.00</b></p>
      <p class="note">Allow 1/2 hr</p>
    </div>
  </div>

  <div class="panel panel--3">
    <div class="photo photo--head" role="img" aria-label="Photo of rolled spa towels"><span class="photo-title">WAXING</span></div>
    <ul class="menu price-list" style="top:142px">
      <li>1/2 leg $25.00</li>
      <li>3/4 leg $35.00</li>
      <li>Full leg $45.00</li>
      <li>1/2 arm $20.00</li>
      <li>Full arm $30.00</li>
      <li>Underarm $16.00</li>
      <li>Lip $10.00</li>
      <li>Chin $12.00</li>
      <li>Chin and Lip $18.00</li>
      <li>Cheek $15.00</li>
      <li>Eyebrow tidy $15.00</li>
      <li>Standard Bikini $18.00</li>
      <li>G String $28.00</li>
      <li>Brazilian (everything off) $40.00</li>
      <li>Stomach $15.00</li>
    </ul>
  </div>
</section>

</body>
</html>
```